Lawn Company needs design work on a service call flyer!

We are a lawn care company that fertilizes and sprays lawns. This design is meant to be left behind at the customers house after a lawn application has been done too let them know what we have done.

The finished design will be printed on A6 paper (4.1 x 5.8 inches)

I have attached PDF files of the text that I want on the front of the document and the back of the document. I also included a sample design that I had been working on to give some idea what I would like. I don't want the same design, but you can use it as a building block for something new or come up with something entirely different.

FRONT: The front of the design is most important.

BACK: Other then the text the design should be minimal. If possible I would like an outline of the trees in my logo to be a backdrop. I have attached a PDF of the back of my business card as an example

The winning design will be a professional looking document that flows and reflects a lawn care business. Please contact me if you have any questions. I will only pick a design that is better then my current template.

Thank You

Target Market(s)

Lawn Care Customers

Industry/Entity Type

Lawn Care

Requirements
Must have
• 1. Our Logo
• 2. The attached text for the front & back of document
• 3. Our phone number (604-918-4471)
• 4. Our Email address (fenwickturfcare@mailora.net)
Nice to have
• A green theme with flowing graphics
Should not have
• any pictures of houses, people, or tools
• Don't copy the text or design from my design template. It is outdated, is it meant to be an example only

```html
<!DOCTYPE html>
<html lang="en">
<head>
<meta charset="utf-8">
<title>Fenwick Turf Care – Service Call Card</title>
<link href="https://fonts.googleapis.com/css2?family=Open+Sans:ital,wght@0,400;0,600;0,700;1,400&display=swap" rel="stylesheet">
<style>
  :root {
    --page-bg: #e4e6df;
    --green: #1f9a3a;
    --green-dark: #1d6b2a;
    --lime: #7cbf35;
    --turf: #3f8a2e;
    --ink: #1e3a22;
    --text: #2b2b2b;
    --white: #ffffff;
  }
  * { box-sizing: border-box; margin: 0; padding: 0; }
  html, body { width: 1200px; height: 800px; overflow: hidden; }
  body {
    background: var(--page-bg);
    font-family: "Open Sans", Arial, sans-serif;
    position: relative;
  }
  .card {
    position: absolute;
    top: 199px;
    width: 570px;
    height: 402px;
    overflow: hidden;
    background: var(--white);
  }
  .card--front { left: 20px; }
  .card--back { left: 610px; }

  /* FRONT */
  .front-scene {
    position: absolute; inset: 0;
    background:
      radial-gradient(circle at 12% 8%, rgba(60,110,200,.85) 0, rgba(60,110,200,0) 26%),
      radial-gradient(circle at 75% 30%, rgba(190,225,245,.9) 0, rgba(190,225,245,0) 40%),
      linear-gradient(180deg, #8fbbe4 0%, #cfe6f2 30%, #e5f1e0 52%, #a9d36a 66%, #4f9c2c 82%, #2f6e1d 100%);
  }
  .brand-panel {
    position: absolute; left: 0; top: 51px;
    width: 250px; height: 253px;
    background: rgba(255,255,255,.55);
    border-radius: 0 14px 14px 0;
    text-align: center;
  }
  .brand-name {
    margin-top: 34px;
    font-size: 26px; font-weight: 700; line-height: 1.05;
    color: var(--green-dark);
    letter-spacing: .5px;
  }
  .brand-name span { display: block; font-size: 15px; letter-spacing: 2px; }
  .brand-mark {
    display: block;
    width: 14px; height: 14px; border-radius: 50%;
    background: var(--green); margin: 0 auto 8px;
  }
  .panel-label {
    color: var(--green); font-weight: 600; font-size: 13px; line-height: 1.3;
  }
  .panel-label--time { margin-top: 34px; }
  .panel-label--by { margin-top: 12px; }
  .blank-line {
    width: 150px; height: 1px; background: var(--green-dark);
    margin: 22px auto 0;
  }
  .application {
    position: absolute; left: 270px; top: 68px; width: 290px;
    color: var(--ink);
  }
  .application h2 { font-size: 13.5px; font-weight: 400; color: var(--green); margin-bottom: 8px; }
  .option { display: flex; align-items: flex-start; gap: 7px; font-size: 12.5px; margin-bottom: 7px; }
  .option .box { width: 15px; height: 15px; background: var(--white); flex: none; margin-top: 1px; }
  .option small { display: block; font-size: 9.5px; }
  .fill-line { display: inline-block; width: 95px; border-bottom: 1px solid var(--ink); }
  .watering { margin-top: 24px; font-size: 12.5px; line-height: 1.55; }
  .pledge {
    margin-top: 28px; font-size: 8.6px; font-style: italic; line-height: 1.42; text-align: justify;
  }

  /* BACK */
  .back-header {
    position: absolute; left: 0; top: 0; width: 100%; height: 48px;
    background: var(--lime);
    color: var(--white); font-size: 14.5px; font-weight: 400;
    padding: 27px 0 0 22px; line-height: 1;
  }
  .guide {
    position: absolute; top: 60px;
    font-size: 8.6px; color: var(--text); line-height: 1.25;
  }
  .guide--water { left: 18px; width: 245px; }
  .guide--mow { left: 280px; width: 272px; }
  .guide h3 { font-size: 11px; font-weight: 600; color: var(--lime); margin-bottom: 3px; }
  .guide .lead { font-size: 9.6px; margin-bottom: 8px; }
  .guide ul { padding-left: 14px; }
  .guide li { margin-bottom: 3px; }
  .tree-art {
    position: absolute; left: 175px; top: 282px; width: 385px; height: 65px;
    background: linear-gradient(90deg, rgba(63,138,46,.15), rgba(63,138,46,.55) 30%, rgba(63,138,46,.65) 70%, rgba(63,138,46,.3));
    border-radius: 30px 30px 0 0;
  }
  .contact-band {
    position: absolute; left: 0; bottom: 0; width: 100%; height: 55px;
    background: linear-gradient(180deg, #4f9a34, var(--turf) 60%, #2f6e22);
    display: flex; align-items: center; gap: 38px; padding-left: 80px;
    color: var(--white); font-size: 15px; font-weight: 600;
  }
  .contact { display: flex; align-items: center; gap: 8px; }
  .contact svg { flex: none; }
</style>
</head>
<body>

<section class="card card--front">
  <div class="front-scene" role="img" aria-label="Soft blue bokeh sky fading into a close-up of fresh green grass blades"></div>

  <div class="brand-panel">
    <p class="brand-name"><i class="brand-mark"></i>FENWICK<span>TURF CARE</span></p>
    <p class="panel-label panel-label--time">Application Time / Date:</p>
    <div class="blank-line"></div>
    <p class="panel-label panel-label--by">Your Lawn has been Professionally<br>Serviced today by:</p>
    <div class="blank-line"></div>
  </div>

  <div class="application">
    <h2>Today's application consists of:</h2>
    <div class="option"><span class="box"></span><span>Seasonally Balanced Slow Release Fertilizer</span></div>
    <div class="option"><span class="box"></span><span>Broadleaf Weed Control<small>(Please keep off the lawn until it is thoroughly dry)</small></span></div>
    <div class="option"><span class="box"></span><span>Other <span class="fill-line"></span></span></div>
    <p class="watering">Please begin watering the lawn<br><span class="fill-line"></span> after application.</p>
    <p class="pledge">“We strive to complete work in a professional manner each and every visit. If you are not satisfied with the level of service you are receiving please contact us. We value your business and wish to maintain long-term relationships with our customers.”</p>
  </div>
</section>

<section class="card card--back">
  <h2 class="back-header">Please follow these general guidelines:</h2>

  <div class="guide guide--water">
    <h3>WATERING YOUR LAWN</h3>
    <p class="lead">Deep, regular watering keeps roots strong and lawns green and lush.</p>
    <ul>
      <li>Water early in the morning so less moisture is lost to heat and wind.</li>
      <li>Aim for about one inch of water per week, including rainfall.</li>
      <li>Water deeply and less often to encourage deep roots.</li>
      <li>Set a tin can in the path of your sprinkler to measure how much water the lawn receives.</li>
      <li>Aerating your lawn helps the soil utilize more water and prevent unnecessary runoff.</li>
    </ul>
  </div>

  <div class="guide guide--mow">
    <h3>MOWING YOUR LAWN</h3>
    <p class="lead">Mowing your lawn properly can make all the difference in how it looks throughout the year</p>
    <ul>
      <li>You should mow your lawn at 2.5 - 3 inches (no shorter). Mowing at this length helps shade your roots and provides more leaf surface for your lawn to manufacture its own food. As an added bonus it will help your lawn retain its moisture and reduce watering requirements.</li>
      <li>As a general rule, try not to remove more then 1/3 of the leaf blade in a single mowing. During periods of heavy growth, this may mean mowing more frequently then usual.</li>
      <li>Always ensure your lawn mower is maintained and the blade is sharp so that is cuts cleanly.</li>
      <li>Your last mowing in the fall should be shorter, about 2 inches.</li>
    </ul>
  </div>

  <div class="tree-art" role="img" aria-label="Row of four grass-textured tree silhouettes through the seasons"></div>

  <div class="contact-band">
    <span class="contact">
      <svg width="28" height="28" viewBox="0 0 28 28" aria-hidden="true">
        <circle cx="14" cy="14" r="12.5" fill="none" stroke="#fff" stroke-width="2"/>
        <path d="M9.5 7.5l3 3-1.8 2c.9 1.9 2.3 3.3 4.2 4.2l2-1.8 3 3-2 2c-5 0-10.4-5.4-10.4-10.4z" fill="#fff"/>
      </svg>
      604-918-4471
    </span>
    <span class="contact">
      <svg width="28" height="28" viewBox="0 0 28 28" aria-hidden="true">
        <circle cx="14" cy="14" r="12.5" fill="none" stroke="#fff" stroke-width="2"/>
        <rect x="7.5" y="9.5" width="13" height="9" fill="none" stroke="#fff" stroke-width="1.6"/>
        <path d="M7.5 9.5l6.5 5 6.5-5M7.5 18.5l4.5-4M20.5 18.5l-4.5-4" fill="none" stroke="#fff" stroke-width="1.4"/>
      </svg>
      fenwickturfcare@mailora.net
    </span>
  </div>
</section>

</body>
</html>
```